Cognitive therapist.

I am a therapist and my main work is with clients who have depression and anxiety disorders.

I need something reasonably plain. Cognitive therapy is a very pragmatic approach to dealing with problems, so it isn't new agey (no offence to new age therapies at all)

Hi everyone, I am currently looking at a particular design that I will most likely go with. Cheers, Mel

Mel Tarrow
Cognitive Therapist
BA, PG Dip Mental Health,
PG Dip Cog Beh Therapy
MKLPT

The Larchmont Rooms,
Level One
57 Quillon Parade
Cnr Fenwick St & Quillon Parade
P O Box 38 215
WELLINGTON 6281

Phone: 027 534 2870 Email: mtarrow@vexmail.co.nz

www.meltarrow.co.nz

• No illustration, or colour. not old style fonts.

```html
<!DOCTYPE html>
<html lang="en">
<head>
<meta charset="utf-8">
<title>Mel Tarrow – Business Card</title>
<link rel="stylesheet" href="https://fonts.googleapis.com/css2?family=Source+Sans+3:wght@400;600&display=swap">
<style>
  :root {
    --page: #e4e4e4;
    --card: #ffffff;
    --band-blue: #0a95c6;
    --band-blue-deep: #067fb0;
    --band-grey: #ececec;
    --accent: #1a9ccc;
    --ink: #3d3d3d;
    --icon: #2a7fb0;
  }
  * { margin: 0; padding: 0; box-sizing: border-box; }
  html, body {
    width: 1200px; height: 1000px; overflow: hidden;
    background: var(--page);
    font-family: "Source Sans 3", "Myriad Pro", Arial, sans-serif;
  }
  .card {
    position: absolute; left: 75px; top: 200px;
    width: 1050px; height: 600px;
    background: var(--card);
    box-shadow: 0 6px 24px rgba(0,0,0,0.18);
    overflow: hidden;
  }
  .band-grey {
    position: absolute; left: 0; top: 150px; width: 100%; height: 68px;
    background: var(--band-grey);
  }
  .band-blue {
    position: absolute; left: 0; top: 45px; width: 100%; height: 108px;
    background: linear-gradient(90deg, var(--band-blue) 0%, var(--band-blue-deep) 100%);
  }
  .name {
    position: absolute; right: 110px; top: 58px;
    font-size: 98px; font-weight: 400; line-height: 1;
    color: #fff; text-transform: uppercase; letter-spacing: 1px;
    text-shadow: 0 0 2px rgba(0,60,90,0.6);
  }
  .credentials {
    position: absolute; right: 40px; top: 166px;
    font-size: 27px; color: var(--accent); white-space: nowrap;
  }
  .contacts {
    position: absolute; left: 50px; top: 268px;
    list-style: none; font-size: 26px; color: var(--ink);
  }
  .contacts li {
    display: flex; align-items: flex-start; gap: 14px;
    line-height: 1.2; margin-bottom: 14px;
  }
  .contacts svg { width: 26px; height: 26px; flex: none; margin-top: 3px; fill: var(--icon); }
  .contacts .address { line-height: 1.45; margin-top: -4px; }
</style>
</head>
<body>
  <div class="card">
    <div class="band-grey"></div>
    <div class="band-blue"></div>
    <h1 class="name">Mel Tarrow</h1>
    <p class="credentials">Cognitive Therapist BA, PG Dip Mental Health, PG Dip Cog Beh Therapy</p>

    <ul class="contacts">
      <li>
        <svg viewBox="0 0 24 24" aria-hidden="true"><path d="M6.6 10.8a15.1 15.1 0 0 0 6.6 6.6l2.2-2.2a1 1 0 0 1 1-.25 11.4 11.4 0 0 0 3.6.57 1 1 0 0 1 1 1V20a1 1 0 0 1-1 1A17 17 0 0 1 3 4a1 1 0 0 1 1-1h3.5a1 1 0 0 1 1 1c0 1.25.2 2.45.57 3.57a1 1 0 0 1-.25 1z"/></svg>
        <span>027 534 2870</span>
      </li>
      <li>
        <svg viewBox="0 0 24 24" aria-hidden="true"><path d="M2 5h20v14H2z" fill="none"/><path d="M2 5h20v14H2V5zm2 2v.4l8 5.2 8-5.2V7H4z"/></svg>
        <span>mtarrow@vexmail.co.nz</span>
      </li>
      <li>
        <svg viewBox="0 0 24 24" aria-hidden="true"><path d="M12 2a10 10 0 1 0 0 20 10 10 0 0 0 0-20zm6.9 6h-3a15.6 15.6 0 0 0-1.4-3.6A8 8 0 0 1 18.9 8zM12 4a14 14 0 0 1 1.9 4h-3.8A14 14 0 0 1 12 4zM4.3 14a8.2 8.2 0 0 1 0-4h3.4a16 16 0 0 0 0 4zm.8 2h3a15.6 15.6 0 0 0 1.4 3.6A8 8 0 0 1 5.1 16zm3-8h-3a8 8 0 0 1 4.4-3.6A15.6 15.6 0 0 0 8.1 8zM12 20a14 14 0 0 1-1.9-4h3.8A14 14 0 0 1 12 20zm2.3-6H9.7a14.7 14.7 0 0 1 0-4h4.6a14.7 14.7 0 0 1 0 4zm.2 5.6a15.6 15.6 0 0 0 1.4-3.6h3a8 8 0 0 1-4.4 3.6zm1.8-5.6a16 16 0 0 0 0-4h3.4a8.2 8.2 0 0 1 0 4z"/></svg>
        <span>www.meltarrow.co.nz</span>
      </li>
      <li>
        <svg viewBox="0 0 24 24" aria-hidden="true"><path d="M12 3 2 12h3v8h5v-5h4v5h5v-8h3z"/></svg>
        <span class="address">The Larchmont Rooms, Level One 57 Quillon Parade,<br>Cnr Fenwick St &amp; Quillon Parade, P O Box 38 215 WELLINGTON 6281.</span>
      </li>
    </ul>
  </div>
</body>
</html>
```